Web design for online activity booking website

Our activity booking website uTrundle.net is looking outdated and needing a loving revamp on its design and STRUCTURE. it was initially created as a destination guide before we modified the homepage slightly to sell activities. So please DON'T RELY on the current website for your design. Now, the focus is ACTIVITY, while guide/ info should come only as secondary.

In other words, we will be doing something very similar to Plomaro.com (a bit crowded for our liking) and FindMyTrailpal.com. If you could capture the best essences of both, that would be awesome! Besides, we also like nestlo.com's simplicity.

SIMPLE, CLEAN, BRIGHT, USER and MOBILE FRIENDLY please :)

We have a new logo created and some wireframes (a few more in progress) so you know the basic components required in each page. These are just rough ideas so please ignore the ratio/size, colours etc and if you have a better way of arranging or simplifying things, please do so :)

Help us make it a website that everyone would love!

Thank you in advance for your time and artistry.

Target Market(s)

Internet savvy travellers between 18-65

Industry/Entity Type

Tourism

Number of Pages Required

5+ page

Requirements
Must have
• SIMPLE, CLEAN feel, USER and MOBILE FRIENDLY please :)
• See attachments for rough structure. Will also need standard pages such as:
• - About Us
• - Contact Us
• - Wishlist etc
• Message from our developer "designer to keep layers in PSD format accurately so html/css code does not need to lead a mess in photoshop"
Nice to have
• UPDATE: We are so thrilled to receive so many web designs but on the other hand, the submissions are getting too generic and everyone's designs is almost looking identical (many look like they are “borrowed” from existing popular websites). This is making the selection and decision process very difficult.
• So instead of sending us more of the very similar homepage design with minor tweaks (which we can do during handover section anyway), please send us a design of more specific page of our website. Please refer job brief, file no. 5 - Product detail page.
• This will give us better idea of your skills and choose the best as winner to work on the rest of our web pages.
Should not have
• No dark background please

```html
<!DOCTYPE html>
<html lang="en">
<head>
<meta charset="utf-8">
<title>uTrundle.net – Book Activities</title>
<link href="https://fonts.googleapis.com/css2?family=Ubuntu:wght@400;500;700&family=Open+Sans:wght@400;600;700&display=swap" rel="stylesheet">
<style>
:root{
  --green:#3cb54a;
  --green-dark:#2f9a3c;
  --red:#d8234b;
  --price:#cf2140;
  --orange:#f0941e;
  --blue:#2ba6c9;
  --ink:#3f3f3f;
  --line:#d9d9d9;
  --page:#e6e6e6;
  --white:#ffffff;
  --star:#e3a400;
  --footer:#f1f1f1;
}
*{box-sizing:border-box;margin:0;padding:0}
html,body{width:679px;height:1200px;overflow:hidden;background:var(--white)}
body{font-family:"Open Sans",Arial,sans-serif;color:var(--ink);position:relative}
.canvas{position:relative;width:679px;height:1200px;overflow:hidden;background:var(--page)}
.abs{position:absolute}
.photo{position:absolute;display:block}

/* hero */
.hero{position:absolute;left:0;top:0;width:679px;height:219px;overflow:hidden}
.hero .photo{inset:0;background:
  radial-gradient(ellipse 70% 45% at 38% 100%,#f2f5f8 0%,#c9dcec 30%,rgba(120,170,220,0) 70%),
  radial-gradient(ellipse 30% 30% at 78% 20%,rgba(40,40,55,.35),rgba(40,40,55,0) 70%),
  radial-gradient(ellipse 14% 12% at 25% 82%,rgba(40,40,55,.3),rgba(40,40,55,0) 70%),
  linear-gradient(180deg,#0f4e9a 0%,#2f78c2 35%,#6aa5dc 65%,#a9cbea 100%)}
.brand{position:absolute;left:118px;top:10px;display:flex;align-items:center;gap:4px;
  font-family:"Ubuntu",sans-serif;font-weight:700;font-size:15px;color:var(--white)}
.brand .dot{width:6px;height:6px;border-radius:50%;background:var(--red)}
.topnav{position:absolute;left:396px;top:9px;display:flex;gap:11px;align-items:center}
.topnav svg{width:11px;height:11px;fill:none;stroke:var(--white);stroke-width:2}
.signup{background:var(--orange);color:var(--white);font-size:5px;padding:2px 4px;border-radius:2px}
.hero-title{position:absolute;left:0;width:679px;top:90px;text-align:center;
  font-family:"Ubuntu",sans-serif;font-weight:700;font-size:29px;color:#e9eef3;text-shadow:0 1px 2px rgba(0,0,0,.35)}
.hero-sub{position:absolute;left:236px;top:123px;width:207px;height:21px;background:rgba(43,166,201,.9);
  text-align:center;font-family:"Ubuntu",sans-serif;font-size:15px;line-height:21px;color:#ecf7fb}
.searchbar{position:absolute;left:122px;top:170px;width:436px;height:31px;background:rgba(255,255,255,.4);
  border-radius:3px;display:flex;align-items:center;gap:4px;padding:0 4px}
.field{height:19px;background:var(--white);font-size:6.3px;color:#555;padding:0 6px;display:flex;align-items:center;justify-content:space-between}
.field.small{font-size:4.5px}
.cal{width:10px;height:10px}
.go{height:22px;width:51px;background:var(--green);color:#f6fff0;font-family:"Ubuntu",sans-serif;font-weight:700;font-size:10px;display:flex;align-items:center;justify-content:center;border-radius:2px}

.section-title{position:absolute;left:0;width:679px;text-align:center;font-family:"Ubuntu",sans-serif;font-weight:400;font-size:14.5px;color:#4a4a4a}

/* destinations */
.dest{position:absolute;width:118px;height:118px;overflow:hidden}
.dest .photo{inset:0}
.dest span{position:absolute;left:0;width:100%;top:54px;text-align:center;font-family:"Ubuntu",sans-serif;font-size:8.5px;color:rgba(255,255,255,.85)}
.dest-btn{position:absolute;left:42px;top:98px;width:74px;height:14px;background:rgba(255,255,255,.8);font-size:4.5px;color:#666;text-align:center;line-height:14px}

/* activities */
.activities{position:absolute;left:0;top:566px;width:679px;height:240px;background:#f5f5f5}
.find{position:absolute;left:317px;top:597px;font-size:4.5px;color:#444;display:flex;gap:3px;align-items:center}
.tabs{position:absolute;left:245px;top:609px;display:flex;gap:48px;font-size:4.6px;color:#555}
.tabs .on{color:var(--orange)}
.card{position:absolute;top:636px;width:106px;height:128px;background:var(--white);box-shadow:0 1px 3px rgba(0,0,0,.25)}
.card.featured{top:626px;height:148px;box-shadow:0 2px 6px rgba(0,0,0,.3)}
.card .pic{position:absolute;left:0;top:0;width:106px;height:70px}
.card .fav{position:absolute;right:8px;top:63px;width:14px;height:14px;border-radius:50%;background:var(--red);display:flex;align-items:center;justify-content:center}
.card.featured .fav{background:var(--green)}
.card .fav svg{width:7px;height:7px;fill:var(--white)}
.card h3{position:absolute;left:6px;top:74px;font-family:"Ubuntu",sans-serif;font-size:8px;font-weight:700;color:#333}
.card .meta{position:absolute;left:6px;top:84px;font-size:3.6px;color:#999}
.card .desc{position:absolute;left:6px;top:90px;width:86px;font-size:3.6px;line-height:4.6px;color:#aaa}
.card .price{position:absolute;left:6px;top:104px;font-family:"Ubuntu",sans-serif;font-size:13px;font-weight:700;color:var(--price)}
.card.featured .price{color:var(--green-dark)}
.card .price sup{font-size:7px}
.stars{position:absolute;left:59px;top:110px;font-size:6px;letter-spacing:.3px;color:var(--star)}
.stars i{font-style:normal;color:#d6d6d6}
.book{position:absolute;left:6px;top:124px;width:94px;height:16px;background:var(--green);color:var(--white);font-size:5px;text-align:center;line-height:16px}
.arrow{position:absolute;top:689px;width:21px;height:21px;border-radius:50%;border:1px solid #888;display:flex;align-items:center;justify-content:center}
.arrow svg{width:7px;height:7px;stroke:#777;stroke-width:1.6;fill:none}

/* map */
.map{position:absolute;left:0;top:806px;width:679px;height:228px;background:
  radial-gradient(ellipse 40% 30% at 70% 10%,rgba(190,170,90,.45),rgba(190,170,90,0) 70%),
  radial-gradient(ellipse 30% 40% at 15% 70%,rgba(150,165,140,.35),rgba(150,165,140,0) 70%),
  radial-gradient(ellipse 35% 35% at 90% 60%,rgba(150,150,150,.5),rgba(150,150,150,0) 70%),
  linear-gradient(160deg,#a8a8a8,#8f8f8f 55%,#9d9d9d)}
.hotspots{position:absolute;left:118px;top:830px;width:121px;height:148px;background:#ececec;box-shadow:0 1px 3px rgba(0,0,0,.3)}
.hotspots h4{font-family:"Ubuntu",sans-serif;font-weight:400;font-size:7px;color:#777;text-align:center;padding:6px 0 4px;border-bottom:1px solid var(--line)}
.hot{display:flex;gap:7px;align-items:center;height:22px;padding-left:6px;font-size:3.8px;color:#444}
.hot b{color:#c9472b;font-size:5.5px;letter-spacing:-.3px}
.popup{position:absolute;left:310px;top:830px;width:212px;height:136px;background:var(--white);box-shadow:0 1px 4px rgba(0,0,0,.3)}
.popup h5{position:absolute;left:29px;top:8px;font-family:"Ubuntu",sans-serif;font-weight:400;font-size:8.5px;color:#333;line-height:10.5px}
.popup .close{position:absolute;right:7px;top:6px;width:10px;height:10px}
.popup .pic{position:absolute;left:0;top:37px;width:212px;height:70px}
.popup .ov{position:absolute;left:8px;top:76px;font-family:"Ubuntu",sans-serif;font-size:10px;color:var(--white)}
.popup .ovtext{position:absolute;left:8px;top:89px;width:194px;font-size:3.6px;line-height:4.4px;color:#eee}
.popup .pstars{position:absolute;left:16px;top:110px;font-size:6px;color:var(--star)}
.popup .dur{position:absolute;left:16px;top:121px;font-size:3.8px;color:#555}
.popup .pprice{position:absolute;left:153px;top:115px;font-family:"Ubuntu",sans-serif;font-weight:700;font-size:11px;color:var(--green-dark)}
.pin{position:absolute;width:20px;height:28px}
.mapsearch{position:absolute;left:118px;top:998px;width:340px;height:29px;background:rgba(255,255,255,.3);display:flex;align-items:center;gap:5px;padding:0 3px}
.mapsearch .input{width:170px;height:19px;background:var(--white);font-size:5.5px;color:#555;padding-left:6px;line-height:19px}
.mapsearch .btn{width:54px;height:19px;background:var(--green);color:var(--white);font-size:7.5px;display:flex;align-items:center;justify-content:center;gap:3px}
.mapsearch .or{font-size:5.5px;color:#444;width:18px;text-align:center}
.mapsearch .near{width:80px;height:19px;background:#e8602e;color:var(--white);font-size:4.4px;display:flex;align-items:center;justify-content:center}

/* newsletter */
.newsletter{position:absolute;left:0;top:1034px;width:679px;height:57px;background:var(--orange)}
.newsletter h6{position:absolute;left:172px;top:15px;font-family:"Ubuntu",sans-serif;font-weight:400;font-size:9.5px;color:#fbe3c1}
.newsletter p{position:absolute;left:172px;top:28px;width:168px;font-size:3.8px;line-height:4.7px;color:#fde9cc}
.newsletter .email{position:absolute;left:345px;top:18px;width:105px;height:16px;background:var(--white);font-size:5px;color:#777;padding-left:7px;line-height:16px}
.newsletter .sub{position:absolute;left:450px;top:18px;width:55px;height:16px;background:var(--blue);font-size:5px;color:var(--white);text-align:center;line-height:16px}

/* footer */
.footer{position:absolute;left:0;top:1091px;width:679px;height:109px;background:var(--footer)}
.fbrand{position:absolute;left:118px;top:18px;display:flex;align-items:center;gap:4px;font-family:"Ubuntu",sans-serif;font-weight:700;font-size:14px;color:#444}
.fbrand .dot{width:6px;height:6px;border-radius:50%;background:var(--red)}
.copy{position:absolute;left:118px;top:38px;font-size:4.8px;color:#888;line-height:6px}
.fcol{position:absolute;top:23px;font-size:5.2px;color:#666;line-height:13.6px}
.fcol strong{display:block;font-weight:400;color:var(--blue);font-size:5.2px}
.social{position:absolute;left:525px;top:23px;width:40px}
.social strong{display:block;font-weight:400;color:var(--blue);font-size:5.2px;text-align:center;margin-bottom:3px}
.social .row{display:flex;gap:3px;margin-bottom:3px;justify-content:center}
.social span{width:16px;height:16px;border-radius:50%}

/* dim layer + modal */
.dim{position:absolute;left:0;top:219px;width:679px;height:815px;background:rgba(120,120,120,.1)}
.modal{position:absolute;left:244px;top:358px;width:191px;height:174px;background:var(--white);box-shadow:0 2px 8px rgba(0,0,0,.35);padding:0 11px}
.modal h2{text-align:center;font-family:"Ubuntu",sans-serif;font-weight:700;font-size:13.5px;color:#111;margin-top:5px}
.modal .tag{text-align:center;font-size:7px;color:#333;margin-bottom:5px}
.m-field{height:15px;border:1px solid #c7c7c7;border-radius:2px;font-size:4px;color:#7f97b8;display:flex;align-items:center;justify-content:space-between;padding:0 4px;margin-bottom:6px;white-space:nowrap}
.m-row{display:flex;gap:10px}
.m-row .m-field{flex:1}
.m-field.plain{color:#777}
.m-book{width:74px;height:13px;margin:3px auto 5px;background:var(--green);color:var(--white);font-size:4.2px;text-align:center;line-height:13px}
.privacy{display:flex;justify-content:center;gap:3px;align-items:center;font-size:3px;color:#888}
.spinner{position:absolute;left:330px;top:534px;width:18px;height:18px}
.note{position:absolute;left:7px;top:382px;width:110px;font-family:Arial,sans-serif;color:var(--white)}
.note b{font-weight:400;font-size:8px;display:block}
.note p{font-size:5.3px;line-height:6px}
.note-line{position:absolute;left:64px;top:387px;width:177px;height:1px;background:var(--white)}
</style>
</head>
<body>
<div class="canvas">

  <header class="hero">
    <div class="photo" role="img" aria-label="Skydivers in free fall above the clouds"></div>
    <div class="brand"><span class="dot"></span>uTrundle</div>
    <nav class="topnav">
      <svg viewBox="0 0 12 12"><path d="M6 10.5 1.5 6A2.6 2.6 0 0 1 6 2.8 2.6 2.6 0 0 1 10.5 6Z"/></svg>
      <svg viewBox="0 0 12 12"><path d="M1 2h2l1.5 6h5.5l1-4.5H4"/><circle cx="5" cy="10.3" r=".7"/><circle cx="9" cy="10.3" r=".7"/></svg>
      <svg viewBox="0 0 12 12"><circle cx="6" cy="6" r="5"/><path d="M1 6h10M6 1c-2.5 3-2.5 7 0 10M6 1c2.5 3 2.5 7 0 10"/></svg>
      <svg viewBox="0 0 12 12"><circle cx="6" cy="6" r="5"/><path d="M7.5 4.3C7 3.6 5 3.5 5 4.8s2.6.9 2.6 2.3S5.5 8.6 4.6 7.7M6 2.8v6.4"/></svg>
      <svg viewBox="0 0 12 12"><circle cx="6" cy="6" r="5"/><path d="M4.7 4.6A1.4 1.4 0 1 1 6 6.3v1"/><circle cx="6" cy="8.8" r=".3"/></svg>
      <svg viewBox="0 0 12 12"><circle cx="6" cy="4" r="2.4"/><path d="M1.5 11c.5-3 8.5-3 9 0"/></svg>
      <span class="signup">Sign Up</span>
    </nav>
    <h1 class="hero-title">BOOK ACTIVITIES</h1>
    <div class="hero-sub">Your Adventure Starts Here!</div>
    <form class="searchbar">
      <div class="field" style="width:104px">Where to, my friend?</div>
      <div class="field" style="width:104px">What would you like to do?</div>
      <div class="field small" style="width:72px">START DATE
        <svg class="cal" viewBox="0 0 10 10"><rect x="1" y="2" width="8" height="7" fill="none" stroke="#555"/><path d="M1 4h8M3 1v2M7 1v2" stroke="#555"/></svg></div>
      <div class="field small" style="width:72px">ADULT X1</div>
      <div class="go">LET'S GO!</div>
    </form>
  </header>

  <h2 class="section-title" style="top:235px">Explore Our Top Destinations</h2>

  <div class="dest" style="left:139px;top:270px"><div class="photo" role="img" aria-label="Monte Carlo coastline with agave plants" style="background:linear-gradient(180deg,#4f86c0 0%,#7a9a8c 22%,#3f7d8f 40%,#2f8aa8 52%,#4f8a4a 68%,#2f6a3a 85%,#7aa05a 100%)"></div><span>MONTE CARLO</span></div>
  <div class="dest" style="left:275px;top:270px"><div class="photo" role="img" aria-label="Bermuda beach with waves and hills" style="background:linear-gradient(170deg,#8e96a0 0%,#7b6a50 30%,#5a4a36 45%,#1f5f80 62%,#5a97a8 78%,#c8d2cc 100%)"></div><span>BERMUDA</span></div>
  <div class="dest" style="left:411px;top:270px"><div class="photo" role="img" aria-label="Italian harbour town at dusk" style="background:linear-gradient(180deg,#1f6fb8 0%,#3d7fbf 25%,#c9c2b4 42%,#8a6a48 58%,#e0b060 68%,#2c5a86 80%,#1d3f66 100%)"></div><span>ITALY</span></div>
  <div class="dest" style="left:139px;top:402px"><div class="photo" role="img" aria-label="Sunset cliffs over the sea" style="background:linear-gradient(180deg,#2c2f55 0%,#6a3c5a 35%,#9c4a4e 55%,#3a2c3c 75%,#231f2c 100%)"></div><div class="dest-btn">ACTIVITIES</div></div>
  <div class="dest" style="left:275px;top:402px"><div class="photo" role="img" aria-label="Destination photo" style="background:linear-gradient(180deg,#3a4f7a,#5a5070 50%,#2a3040)"></div></div>
  <div class="dest" style="left:411px;top:402px"><div class="photo" role="img" aria-label="New York waterfront at sunset" style="background:linear-gradient(180deg,#2d6a98 0%,#6f9ab0 25%,#e2a24a 45%,#a86a3a 55%,#2f6f8f 70%,#1c4a68 100%)"></div><span style="top:56px">NEW YORK</span></div>

  <section class="activities"></section>
  <h2 class="section-title" style="top:572px">Explore Our Top Activities</h2>
  <div class="find"><svg width="6" height="6" viewBox="0 0 6 6"><circle cx="2.5" cy="2.5" r="1.8" fill="none" stroke="#333" stroke-width=".9"/><path d="M3.8 3.8 5.6 5.6" stroke="#333" stroke-width=".9"/></svg>Type to search ...</div>
  <div class="tabs"><span class="on">RECOMMENDED</span><span>DESTINATION</span><span>MOST POPULAR</span></div>

  <div class="arrow" style="left:89px"><svg viewBox="0 0 8 8"><path d="M5.5 1 2.5 4l3 3"/></svg></div>
  <div class="arrow" style="left:569px"><svg viewBox="0 0 8 8"><path d="M2.5 1l3 3-3 3"/></svg></div>

  <article class="card featured" style="left:118px">
    <div class="pic" role="img" aria-label="Snorkellers in clear blue water" style="background:linear-gradient(180deg,#0f5f9e 0%,#2b8fd0 30%,#4aa6d8 50%,#1d6aa8 75%,#0e4a80 100%)"></div>
    <div class="fav"><svg viewBox="0 0 10 10"><path d="M5 9 1 5a2.3 2.3 0 0 1 4-2.6A2.3 2.3 0 0 1 9 5Z"/></svg></div>
    <h3>Deep Sea Diving</h3>
    <div class="meta">8 DAYS, 7 NIGHTS TOUR</div>
    <p class="desc">Reef dives with a local guide, gear and lunch included.</p>
    <div class="price"><sup>$</sup>873</div>
    <div class="stars">★★★<i>★★</i></div>
    <div class="book">BOOK NOW</div>
  </article>
  <article class="card" style="left:231px">
    <div class="pic" role="img" aria-label="Rider on a horse at the beach" style="background:linear-gradient(180deg,#e4e7ea 0%,#d2dde3 45%,#a8bcc6 62%,#8a7a68 80%,#c9c2b2 100%)"></div>
    <div class="fav"><svg viewBox="0 0 10 10"><path d="M5 9 1 5a2.3 2.3 0 0 1 4-2.6A2.3 2.3 0 0 1 9 5Z"/></svg></div>
    <h3>Horseback Riding</h3>
    <div class="meta">8 DAYS, 7 NIGHTS TOUR</div>
    <p class="desc">Ride along quiet shores with a friendly local guide.</p>
    <div class="price"><sup>$</sup>873</div>
    <div class="stars">★★★<i>★★</i></div>
  </article>
  <article class="card" style="left:343px">
    <div class="pic" role="img" aria-label="Person gliding on a jungle zipline" style="background:linear-gradient(160deg,#2f5a22 0%,#5f8a3a 35%,#a09070 55%,#4a7a30 75%,#2a4a1c 100%)"></div>
    <div class="fav"><svg viewBox="0 0 10 10"><path d="M5 9 1 5a2.3 2.3 0 0 1 4-2.6A2.3 2.3 0 0 1 9 5Z"/></svg></div>
    <h3>Amazon Gliding</h3>
    <div class="meta">8 DAYS, 7 NIGHTS TOUR</div>
    <p class="desc">Soar over the rainforest canopy on long safe lines.</p>
    <div class="price"><sup>$</sup>873</div>
    <div class="stars">★★★<i>★★</i></div>
  </article>
  <article class="card" style="left:456px">
    <div class="pic" role="img" aria-label="Cyclist on a forest trail" style="background:linear-gradient(180deg,#3f6a2a 0%,#6a8f40 35%,#8aa050 55%,#9a8a60 80%,#b0a07a 100%)"></div>
    <div class="fav"><svg viewBox="0 0 10 10"><path d="M5 9 1 5a2.3 2.3 0 0 1 4-2.6A2.3 2.3 0 0 1 9 5Z"/></svg></div>
    <h3>Biking in Negril</h3>
    <div class="meta">8 DAYS, 7 NIGHTS TOUR</div>
    <p class="desc">Pedal coastal roads and hidden trails at your own pace.</p>
    <div class="price"><sup>$</sup>873</div>
    <div class="stars">★★★<i>★★</i></div>
  </article>

  <section class="map" role="img" aria-label="Street map of the city with activity hotspots"></section>
  <svg class="pin" style="left:258px;top:838px" viewBox="0 0 20 28"><path d="M10 27C4 18 1 14 1 10a9 9 0 0 1 18 0c0 4-3 8-9 17Z" fill="#7a3c7a"/><circle cx="10" cy="10" r="5" fill="#fff"/></svg>
  <svg class="pin" style="left:538px;top:872px" viewBox="0 0 20 28"><path d="M10 27C4 18 1 14 1 10a9 9 0 0 1 18 0c0 4-3 8-9 17Z" fill="#c42a48"/><circle cx="10" cy="10" r="5" fill="#fff"/></svg>

  <aside class="hotspots">
    <h4>Activities Hot Spot</h4>
    <div class="hot"><b>★★★★★</b>Top things to do in Tenerife</div>
    <div class="hot"><b>★★★★★</b>Top things to do in Barcelona</div>
    <div class="hot"><b>★★★★★</b>Top things to do in Paris</div>
    <div class="hot"><b>★★★★★</b>Top things to do in London</div>
    <div class="hot"><b>★★★★★</b>Top things to do in Berlin</div>
    <div class="hot"><b>★★★★★</b>Top things to do in Kuala</div>
  </aside>

  <div class="popup">
    <svg class="abs" style="left:8px;top:12px;width:14px;height:14px" viewBox="0 0 10 10"><path d="M5 9 1 5a2.3 2.3 0 0 1 4-2.6A2.3 2.3 0 0 1 9 5Z" fill="#555"/></svg>
    <h5>Wandmakers Film Studio Tour<br>London, England</h5>
    <svg class="close" viewBox="0 0 10 10"><path d="M1 1l8 8M9 1 1 9" stroke="#888" stroke-width="1.2"/></svg>
    <div class="pic" role="img" aria-label="London street with a red building" style="background:linear-gradient(90deg,#5a5e66 0%,#7a7f86 30%,#9a3a30 48%,#b04434 55%,#6a6e74 70%,#8a9096 100%)"></div>
    <div class="abs" style="left:0;top:72px;width:212px;height:35px;background:linear-gradient(180deg,rgba(0,0,0,0),rgba(0,0,0,.55))"></div>
    <div class="ov">Overview</div>
    <p class="ovtext">Take the bus from central London for this magical full-day tour of the film studio. Go behind the scenes, explore the enchanting props and costumes, and walk in the footsteps of your favourite characters.</p>
    <div class="pstars">★★★<span style="color:#ccc">★★</span></div>
    <div class="dur">◷ Duration: 7 hours</div>
    <div class="pprice">$78</div>
    <svg class="abs" style="left:192px;top:118px;width:9px;height:6px" viewBox="0 0 9 6"><path d="M1 1l3.5 3.5L8 1" stroke="#2b6cb0" stroke-width="1.4" fill="none"/></svg>
  </div>

  <form class="mapsearch">
    <div class="input">Search for hotspot by town, postcode etc.</div>
    <div class="btn"><svg width="7" height="7" viewBox="0 0 7 7"><circle cx="3" cy="3" r="2.2" fill="none" stroke="#fff"/><path d="M4.6 4.6 6.6 6.6" stroke="#fff"/></svg>Search</div>
    <span class="or">or</span>
    <div class="near">Find a Hot spot near me</div>
  </form>

  <section class="newsletter">
    <h6>Subscribe to our Newsletter</h6>
    <p>Discover exciting travel tips, city guides, and top deals every week on uTrundle.</p>
    <div class="email">enter your email here</div>
    <div class="sub">SUBSCRIBE</div>
  </section>

  <footer class="footer">
    <div class="fbrand"><span class="dot"></span>uTrundle</div>
    <div class="copy">© 2015, uTrundle, LLC.<br>All Rights Reserved.</div>
    <div class="fcol" style="left:212px"><strong>COMPANY</strong>About uTrundle.net<br>Corporate info<br>Blog<br>Careers</div>
    <div class="fcol" style="left:293px"><strong>SUPPORT</strong>Contact us<br>FAQs<br>Legal<br>Privacy Policy<br>Legal</div>
    <div class="fcol" style="left:364px"><strong>PARTNERSHIPS</strong>Supplier sign-up<br>Affiliate Programs</div>
    <div class="fcol" style="left:452px"><strong>LOG-INS</strong>Customers<br>Suppliers<br>Affiliates</div>
    <div class="social"><strong>SOCIAL</strong>
      <div class="row"><span style="background:#3aa1d8"></span><span style="background:#3b5b98"></span></div>
      <div class="row"><span style="background:#d3362c"></span><span style="background:#2677b0"></span></div>
    </div>
  </footer>

  <div class="dim"></div>

  <div class="note-line"></div>
  <div class="note"><b>Booking Form</b><p>Activated by "Book Now" button within focused destination photo. Prefilled with destination and activity selected by the user. User now enters information and submit for booking. Esc/Clicking outside the box cancels the form.</p></div>

  <form class="modal">
    <h2>BOOK ACTIVITIES</h2>
    <p class="tag">Your Adventure Starts Here!</p>
    <div class="m-field">WANDMAKERS FILM STUDIO TOUR AND TRANSFERS<span style="color:#333">▾</span></div>
    <div class="m-field">LONDON, ENGLAND<span style="color:#333">▾</span></div>
    <div class="m-row">
      <div class="m-field plain">DECEMBER 1, 2015
        <svg width="9" height="9" viewBox="0 0 10 10"><rect x="1" y="2" width="8" height="7" fill="none" stroke="#555"/><path d="M1 4h8M3 1v2M7 1v2" stroke="#555"/></svg></div>
      <div class="m-field plain">ADULT X1</div>
    </div>
    <div class="m-row">
      <div class="m-field plain">YOUR NAME</div>
      <div class="m-field plain">EMAIL ADDRESS</div>
    </div>
    <div class="m-field plain" style="justify-content:flex-start;gap:6px;padding-right:0"><span>JAMAICA (+1876) ▾</span><span style="border-left:1px solid #ccc;padding-left:4px;height:100%;line-height:13px">ENTER YOUR PHONE NUMBER</span></div>
    <div class="m-book">BOOK NOW</div>
    <div class="privacy"><svg width="5" height="6" viewBox="0 0 5 6"><rect x=".5" y="2.5" width="4" height="3.3" fill="#777"/><path d="M1.3 2.6V1.7a1.2 1.2 0 0 1 2.4 0v.9" fill="none" stroke="#777" stroke-width=".6"/></svg>WE VALUE YOUR PRIVACY</div>
  </form>

  <svg class="spinner" viewBox="0 0 18 18"><path d="M9 2a7 7 0 1 1-7 7" fill="none" stroke="#2b78c6" stroke-width="2" stroke-linecap="round"/></svg>
</div>
</body>
</html>
```